Business Card for my building company

I would like the card to make a statement, so as soon as you see the card you think "wow nice card' and then read the details on the card its self. Also i would like to be able to put in the detail for the MUST HAVES so please Crete a box that i can alter depending on who in my business needs the cards. Thank you

Target Market(s)

Any one looking to build a house/ townhouse or duplex

Industry/Entity Type

Home Builder

Contact Information for Business Card

I would like the card to have the logo on the card and the must haves

Font styles to use
Sans Serif

Requirements
Must have
• Name
• Phone Number
• Email Address
• Website
• Licence Number
• Abn

```html
<!DOCTYPE html>
<html lang="en">
<head>
<meta charset="utf-8">
<title>Ridgeway Builders – Business Card</title>
<link href="https://fonts.googleapis.com/css2?family=Open+Sans:wght@400;600;700&display=swap" rel="stylesheet">
<style>
  :root {
    --page-bg: #2b2620;
    --card-top: #2a2a2a;
    --card-bottom: #050505;
    --gold: #c9a45a;
    --white: #f4f4f4;
    --muted: #cfcfcf;
    --rule: #6a6a6a;
  }
  * { margin: 0; padding: 0; box-sizing: border-box; }
  html, body {
    width: 1200px; height: 1022px; overflow: hidden;
    background: var(--page-bg);
    font-family: "Open Sans", Arial, sans-serif;
  }
  .stage {
    width: 1200px; height: 1022px;
    display: flex; align-items: center; justify-content: center;
  }
  .card {
    position: relative;
    width: 1000px; height: 580px;
    border-radius: 36px;
    background: linear-gradient(160deg, var(--card-top) 0%, #111 45%, var(--card-bottom) 100%);
    box-shadow: 0 30px 60px rgba(0,0,0,.6);
    display: flex; align-items: center;
    padding: 0 70px;
    overflow: hidden;
  }
  .brand {
    width: 430px;
    display: flex; flex-direction: column; align-items: flex-start; gap: 22px;
  }
  .brand-mark {
    display: flex; align-items: center; gap: 18px;
  }
  .brand-square {
    width: 58px; height: 58px; background: var(--gold);
  }
  .brand-name {
    color: var(--gold);
    font-weight: 700;
    font-size: 44px;
    line-height: 1.05;
    text-transform: uppercase;
  }
  .licence {
    color: var(--white);
    font-size: 24px;
    letter-spacing: 1px;
    padding-left: 76px;
  }
  .divider {
    width: 2px; height: 300px;
    background: linear-gradient(to bottom, transparent, var(--rule), transparent);
    margin: 0 56px 0 10px;
  }
  .details { color: var(--white); }
  .person-name {
    font-size: 44px; font-weight: 700; letter-spacing: 1px; text-transform: uppercase;
  }
  .person-role {
    color: var(--gold); font-size: 20px; letter-spacing: 2px; text-transform: uppercase;
    margin-bottom: 20px;
  }
  .detail-line {
    display: flex; align-items: center; gap: 12px;
    font-size: 22px; color: var(--muted); line-height: 1.75;
  }
  .detail-line svg { width: 18px; height: 18px; fill: var(--gold); flex: none; }
  .detail-line.plain { padding-left: 0; }
</style>
</head>
<body>
<main class="stage">
  <section class="card">
    <div class="brand">
      <div class="brand-mark">
        <span class="brand-square"></span>
        <span class="brand-name">Ridgeway<br>Builders</span>
      </div>
      <p class="licence">#LIC : 1234567</p>
    </div>
    <div class="divider"></div>
    <div class="details">
      <h1 class="person-name">Liam Harlow</h1>
      <p class="person-role">Director</p>
      <p class="detail-line plain">Baymont QLD 4099</p>
      <p class="detail-line plain">ABN : 12 345 678 901</p>
      <p class="detail-line">
        <svg viewBox="0 0 24 24" aria-hidden="true"><path d="M6.6 10.8a15 15 0 0 0 6.6 6.6l2.2-2.2a1 1 0 0 1 1-.25 11.4 11.4 0 0 0 3.6.57 1 1 0 0 1 1 1V20a1 1 0 0 1-1 1A17 17 0 0 1 3 4a1 1 0 0 1 1-1h3.5a1 1 0 0 1 1 1c0 1.25.2 2.45.57 3.57a1 1 0 0 1-.25 1z"/></svg>
        0400 123 456
      </p>
      <p class="detail-line">
        <svg viewBox="0 0 24 24" aria-hidden="true"><path d="M2 5h20v14H2zm2 2v.5l8 5 8-5V7zm0 2.9V17h16V9.9l-8 5z"/></svg>
        info@liamharlow.com
      </p>
      <p class="detail-line">
        <svg viewBox="0 0 24 24" aria-hidden="true"><path d="M12 2a10 10 0 1 0 0 20 10 10 0 0 0 0-20zm6.9 6h-3a15 15 0 0 0-1.3-3.9A8 8 0 0 1 18.9 8zM12 4c.9 1.2 1.6 2.5 2 4h-4c.4-1.5 1.1-2.8 2-4zM4.3 14a8 8 0 0 1 0-4h3.4a16 16 0 0 0 0 4zm.8 2h3a15 15 0 0 0 1.3 3.9A8 8 0 0 1 5.1 16zm3-8h-3a8 8 0 0 1 4.3-3.9A15 15 0 0 0 8.1 8zM12 20c-.9-1.2-1.6-2.5-2-4h4c-.4 1.5-1.1 2.8-2 4zm2.3-6H9.7a14 14 0 0 1 0-4h4.6a14 14 0 0 1 0 4zm.3 5.9a15 15 0 0 0 1.3-3.9h3a8 8 0 0 1-4.3 3.9zm1.7-5.9a16 16 0 0 0 0-4h3.4a8 8 0 0 1 0 4z"/></svg>
        www.ridgewaybuilders.com
      </p>
    </div>
  </section>
</main>
</body>
</html>
```